TRIVEL Corp Has New Logo Now Needs New Stationary

We just chose our new logo, and now we need a letterhead and envelope design. I would like both to be used via Microsoft Word so I can print both the letterhead and envelopes myself rather than having to the letterhead and envelopes produced by a printing firm. I has attached the new logo and spec sheet provided by the logo designer.

```html
<!DOCTYPE html>
<html lang="en">
<head>
<meta charset="utf-8">
<title>TRIVEL Corp Foundation – Letterhead</title>
<link href="https://fonts.googleapis.com/css2?family=Exo+2:wght@300;400;600;700&display=swap" rel="stylesheet">
<style>
  :root {
    --bg: #ececec;
    --paper: #f7f7f7;
    --blue: #5ab0e0;
    --green: #86bf52;
    --ink: #3a3a3a;
    --muted: #8c8c8c;
    --light: #b5b5b5;
  }
  * { margin: 0; padding: 0; box-sizing: border-box; }
  html, body { width: 1200px; height: 1000px; overflow: hidden; background: var(--bg); }
  body { font-family: "Exo 2", sans-serif; color: var(--ink); }

  .letterhead {
    position: absolute; left: 282px; top: 50px;
    width: 636px; height: 900px;
    background: var(--paper);
    box-shadow: 0 8px 30px rgba(0,0,0,.12);
    overflow: hidden;
  }
  .band-top { position: absolute; left: 0; top: 0; width: 100%; height: 12px; background: var(--blue); }
  .band-right { position: absolute; right: 0; top: 0; width: 16px; height: 250px; background: var(--blue); }
  .bracket-left { position: absolute; left: 0; top: 530px; width: 16px; height: 300px; background: var(--green); }
  .bracket-foot { position: absolute; left: 0; top: 814px; width: 150px; height: 16px; background: var(--green); }

  .brand { position: absolute; left: 44px; top: 58px; display: flex; align-items: center; gap: 10px; }
  .brand-dot { width: 22px; height: 22px; border-radius: 50%; background: var(--green); }
  .brand-name { font-weight: 700; font-size: 26px; letter-spacing: 1px; color: var(--ink); line-height: 1; }
  .brand-sub { position: absolute; left: 76px; top: 90px; font-size: 9px; letter-spacing: 6px; color: var(--ink); font-weight: 400; }

  .contact { position: absolute; left: 452px; top: 150px; font-size: 8px; line-height: 12px; color: var(--ink); font-style: normal; }
  .contact-org { font-weight: 600; font-size: 8.5px; margin-bottom: 1px; letter-spacing: .2px; }
  .contact-row { display: flex; gap: 4px; align-items: flex-start; }
  .contact-row svg { width: 8px; height: 8px; margin-top: 2px; flex: none; fill: var(--blue); }
  .contact-indent { padding-left: 12px; }

  .meta { position: absolute; left: 40px; top: 262px; width: 104px; text-align: right; font-size: 9px; line-height: 11px; }
  .meta-label { color: var(--blue); font-weight: 700; text-transform: uppercase; letter-spacing: .5px; }
  .meta-value { color: var(--muted); margin-bottom: 3px; }

  .letter { position: absolute; left: 166px; top: 268px; width: 400px; font-size: 8.6px; line-height: 14px; color: var(--muted); }
  .letter-title { font-size: 15px; line-height: 20px; margin-bottom: 16px; color: var(--light); font-weight: 300; white-space: nowrap; }
  .letter-title strong { color: var(--blue); font-weight: 600; }
  .letter p { margin-bottom: 14px; text-align: justify; }

  .sign-off { position: absolute; left: 400px; top: 660px; text-align: center; width: 150px; }
  .sign-role { font-size: 9px; color: var(--muted); margin-bottom: 6px; }
  .signature { width: 150px; height: 42px; border-radius: 4px; background: linear-gradient(90deg, #e4e4e4, #ececec); }
</style>
</head>
<body>
  <main class="letterhead">
    <div class="band-top"></div>
    <div class="band-right"></div>
    <div class="bracket-left"></div>
    <div class="bracket-foot"></div>

    <header class="brand">
      <span class="brand-dot"></span>
      <span class="brand-name">TRIVEL CORP</span>
    </header>
    <div class="brand-sub">FOUNDATION</div>

    <address class="contact">
      <div class="contact-org">TRIVEL CORP FOUNDATION</div>
      <div class="contact-row"><svg viewBox="0 0 10 10"><path d="M5 0a3.5 3.5 0 0 0-3.5 3.5C1.5 6 5 10 5 10s3.5-4 3.5-6.5A3.5 3.5 0 0 0 5 0zm0 5a1.5 1.5 0 1 1 0-3 1.5 1.5 0 0 1 0 3z"/></svg><span>48 Harbor Lane, Westfield,</span></div>
      <div class="contact-indent">Postal Code, Country</div>
      <div class="contact-row"><svg viewBox="0 0 10 10"><path d="M2 0h2l1 3-1.5 1a6 6 0 0 0 2.5 2.5L7 5l3 1v2a2 2 0 0 1-2 2A8 8 0 0 1 0 2a2 2 0 0 1 2-2z"/></svg><span>555-0192-44</span></div>
      <div class="contact-row"><svg viewBox="0 0 10 10"><path d="M0 2h10v6H0z"/></svg><span>555-0192-45</span></div>
      <div class="contact-row"><svg viewBox="0 0 10 10"><circle cx="5" cy="5" r="5"/></svg><span>www.trivelcorp.example</span></div>
    </address>

    <aside class="meta">
      <div class="meta-label">Subject</div>
      <div class="meta-value">lorem ipsum</div>
      <div class="meta-label">Date</div>
      <div class="meta-value">01/01/2014</div>
      <div class="meta-label">Adressed to</div>
      <div class="meta-value">Anna Reed</div>
    </aside>

    <article class="letter">
      <h1 class="letter-title"><strong>Nulla sodales:</strong> Lorem ipsum dolor sit ametconsectetur.</h1>
      <p>Dear Client,</p>
      <p>Lorem ipsum dolor sit amet, consectetur adipiscing elit. Nulla sodales nisi vitae lorem ipsum dolor sit amet, consectetur adipiscing elit. Suspendisse feugiat eros nisi, a facilisis risus eleifend sed. Aliquam mauris enim, fermentum eu lacinia sit amet, laoreet eu leo. Nullam eleifend nulla in libero tristique, ac vulputate odio tincidunt. Etiam non condimentum tortor. Integer suscipit neque nec odio porttitor cursus.</p>
      <p>Ut vitae interdum diam, in euismod ante. Pellentesque volutpat risus sit amet sodales hendrerit. Mi turpis vulputate dolor, eget cursus nulla eros nec tellus. Nulla tincidunt molestie libero vel pretium. Donec condimentum nulla sit amet risus semper imperdiet. Duis congue eros nec diam blandit, et pellentesque sapien auctor.</p>
      <p>Best regards,</p>
    </article>

    <footer class="sign-off">
      <div class="sign-role">Director</div>
      <div class="signature" role="img" aria-label="Handwritten signature of Mark Ellison"></div>
    </footer>
  </main>
</body>
</html>
```